Dental Office Needs- Flyer Design for Same Day Crowns

We need a flyer that will explain the benefits of the same day crown from the patient prospective. Not show pictures of the machine that makes the crowns. See attached material for content. The flyer should use the practices PMS colors of Green 562 and Blue 3025. The ad should say to the patient - I want to go this office and get my crown done there.
Updates

Project Deadline Extended Reason: The difference in the time zone between USA and Europe has caused issues. Minor changes still need to be worked out. Added Thursday, July 14, 2016

Target Market(s)

Dental Patients

Industry/Entity Type

Dental

Requirements
Must have
• Call to Action
• Business Address and Business Logo
• Classic Design
• images of a Happy 50 year old Couple
• Gives the benefits of the same day crown
Should not have
• No Images of tooth figures
• No before or after pictures

```html
<!DOCTYPE html>
<html lang="en">
<head>
<meta charset="utf-8">
<title>Brookfield Dental Care – Brochure</title>
<link rel="stylesheet" href="https://fonts.googleapis.com/css2?family=Cinzel:wght@700&family=Nunito+Sans:wght@400;700&display=swap">
<style>
  :root{
    --green:#0a8a70;
    --blue:#0b5a87;
    --blue-text:#13507a;
    --white:#ffffff;
    --map-bg:#ece9e2;
    --map-park:#cfe3b8;
  }
  *{margin:0;padding:0;box-sizing:border-box}
  html,body{width:1200px;height:927px;overflow:hidden;background:var(--white)}
  .brochure{position:relative;width:1200px;height:927px;font-family:"Nunito Sans",sans-serif}

  /* Left panel */
  .contact-panel{position:absolute;left:0;top:0;width:401px;height:927px;background:var(--white)}
  .contact-title{position:absolute;left:40px;top:60px;font-family:"Cinzel",serif;font-weight:700;font-size:38px;color:var(--green);letter-spacing:.5px}
  .contact-phone{position:absolute;left:39px;top:144px;font-weight:700;font-size:50px;line-height:60px;color:var(--blue-text)}
  .contact-line{position:absolute;left:41px;font-weight:700;font-size:21px;line-height:26px;color:var(--blue-text)}
  .contact-web{top:206px}
  .contact-mail{top:238px}
  .contact-address{position:absolute;left:40px;top:316px;font-style:normal;font-weight:700;font-size:33px;line-height:40px;color:var(--blue-text)}
  .location-map{position:absolute;left:0;top:430px;width:401px;height:324px;background:linear-gradient(160deg,var(--map-bg) 0%,var(--map-bg) 70%,var(--map-park) 100%)}
  .brand-small{position:absolute;left:0;top:800px;width:401px;text-align:center;font-weight:400;font-size:21px;color:var(--blue-text)}
  .brand-small .mark{display:block;width:14px;height:14px;border-radius:50%;background:var(--blue-text);margin:0 auto 38px}

  /* Middle panel */
  .info-panel{position:absolute;left:401px;top:0;width:398px;height:927px;background:var(--blue);color:var(--white)}
  .section-band{position:absolute;left:0;width:398px;background:var(--green);font-family:"Cinzel",serif;font-weight:700;font-size:18px;letter-spacing:.3px;padding-left:37px;display:flex;align-items:center}
  .band-appointment{top:54px;height:59px}
  .band-finance{top:637px;height:57px}
  .info-text{position:absolute;left:37px;width:326px;font-size:16px;line-height:20px;text-align:justify;hyphens:auto}
  .info-text p{margin-bottom:20px}
  .appointment-text{top:129px}
  .finance-text{top:712px}
  .hours{position:absolute;left:37px;top:488px;font-size:16px;line-height:24px}
  .hours h3{font-size:17px;font-weight:700;margin-bottom:6px}
  .hours b{font-weight:700}

  /* Right panel */
  .cover-panel{position:absolute;left:799px;top:0;width:401px;height:927px}
  .cover-photo{position:absolute;inset:0;background:linear-gradient(180deg,#ffffff 0%,#ffffff 24%,#dfe8df 36%,#a9c07e 55%,#c9b89a 72%,#dcd3bf 88%,#e8e6dc 100%)}
  .brand-cover{position:absolute;left:0;top:74px;width:401px;text-align:center}
  .brand-cover .mark{display:block;width:20px;height:20px;border-radius:50%;background:var(--blue-text);margin:0 auto 28px}
  .brand-cover .name{font-weight:400;font-size:31px;line-height:36px;color:var(--blue-text)}
  .cta{position:absolute;left:49px;top:714px;width:300px;text-align:center;font-family:"Cinzel",serif;font-weight:700;line-height:1}
  .cta span{display:block}
  .cta-small{font-size:17px;color:var(--green)}
  .cta-crowns{font-size:28px;color:var(--green);margin-top:1px}
  .cta-contact{font-size:38px;color:var(--green);margin-top:2px}
  .cta-today{font-size:21px;color:var(--green);margin-top:0}
  .cta-phone{font-size:48px;color:var(--blue-text);margin-top:2px}
</style>
</head>
<body>
<main class="brochure">

  <section class="contact-panel">
    <h2 class="contact-title">CONTACT INFO</h2>
    <div class="contact-phone">555.204.7310</div>
    <div class="contact-line contact-web">www.brookfielddentalcare.com</div>
    <div class="contact-line contact-mail">info@brookfielddentalcare.com</div>
    <address class="contact-address">418 W. Maple Rd.<br>Fairview, MI 48000</address>
    <div class="location-map" role="img" aria-label="Street map showing the office location on W. Maple Rd."></div>
    <div class="brand-small"><span class="mark"></span>Brookfield Dental Care</div>
  </section>

  <section class="info-panel">
    <h2 class="section-band band-appointment">HOW TO GET AN APPOINTMENT</h2>
    <div class="info-text appointment-text">
      <p>All services are performed by appointment only and are made for your individual needs. In order to make your time special, please call in advance so that we may schedule a time convenient for you.</p>
      <p>We will contact you either by phone or email 48 hours prior to your scheduled appointment to answer any questions that you may have regarding your appointment.</p>
      <p>If you cannot keep an appointment or need to reschedule, we ask that you kindly give at least 24-48 hours notice. This courtesy on your part makes it possible for another patient to utilize that appointment time.</p>
    </div>
    <div class="hours">
      <h3>OFFICE HOURS:</h3>
      <div><b>Monday:</b> 7 am - 5 pm</div>
      <div><b>Tuesday:</b> 8 am - 6 pm</div>
      <div><b>Wednesday:</b> 8 am - 6 pm</div>
      <div><b>Thursday:</b> 8 am - 1 pm</div>
    </div>
    <h2 class="section-band band-finance">MULTIPLE FINANCIAL OPTIONS</h2>
    <div class="info-text finance-text">
      <p>We offer several payment options to make your dental care affordable. We offer third party financing through CarePlus Pay®. CarePlus Pay® can help to pay for dental treatment your dental insurance doesn’t cover. They offer no interest financing or low monthly payment options, so you can get what you want when you need it.</p>
    </div>
  </section>

  <section class="cover-panel">
    <div class="cover-photo" role="img" aria-label="Photo of a smiling couple in their fifties sitting outdoors behind a wicker picnic basket"></div>
    <div class="brand-cover">
      <span class="mark"></span>
      <div class="name">Brookfield Dental Care</div>
    </div>
    <div class="cta">
      <span class="cta-small">FOR MORE INFORMATION ABOUT</span>
      <span class="cta-crowns">SAME DAY CROWNS,</span>
      <span class="cta-contact">CONTACT OUR</span>
      <span class="cta-today">DENTAL OFFICE TODAY:</span>
      <span class="cta-phone">555 204 7310</span>
    </div>
  </section>

</main>
</body>
</html>
```